Banner and Overlay for my twicth channel*

I need an overlay and banner for my twitch channel. My channel mostly play card game and some shooting game. I would like to see designs that use Yellow and Black. You can put something like skull and card in the designs. My channel name is KORVINE_Q.

Font styles to use
Sans Serif

Colors
ffffff

```html
<!DOCTYPE html>
<html lang="en">
<head>
<meta charset="utf-8">
<title>KORVINE_Q Stream Overlay</title>
<link href="https://fonts.googleapis.com/css2?family=Montserrat:wght@600;700;800;900&display=swap" rel="stylesheet">
<style>
  :root {
    --bg-deep: #02040c;
    --bg-navy: #0a1230;
    --navy: #101a4a;
    --gold: #f5a800;
    --gold-light: #f7c24a;
    --yellow: #f2c81e;
    --white: #ffffff;
    --panel-top: #2b3552;
    --panel-bottom: #0f1a3c;
  }
  * { margin: 0; padding: 0; box-sizing: border-box; }
  html, body { width: 1200px; height: 675px; overflow: hidden; background: var(--bg-deep); }
  .overlay {
    position: relative; width: 1200px; height: 675px; overflow: hidden;
    font-family: "Montserrat", sans-serif; color: var(--white);
    background:
      radial-gradient(ellipse at 45% 50%, #0d1a45 0%, transparent 55%),
      radial-gradient(ellipse at 80% 60%, #0b1538 0%, transparent 50%),
      var(--bg-deep);
  }
  .offline-screen {
    position: absolute; left: 17px; top: 147px; width: 697px; height: 380px;
    background:
      radial-gradient(circle at 20% 75%, rgba(242,200,30,.55) 0%, transparent 18%),
      radial-gradient(circle at 50% 15%, rgba(245,140,0,.45) 0%, transparent 16%),
      radial-gradient(circle at 48% 90%, rgba(245,160,0,.5) 0%, transparent 18%),
      radial-gradient(circle at 80% 75%, rgba(245,150,0,.35) 0%, transparent 16%),
      linear-gradient(135deg, #0a1236 0%, #050919 50%, #0b1640 100%);
  }
  .offline-title {
    position: absolute; left: 0; right: 0; top: 168px; text-align: center;
    font-weight: 900; font-size: 34px; letter-spacing: 1px; line-height: 1;
    color: #e6e6e6;
  }
  .offline-status {
    position: absolute; left: 330px; top: 217px;
    font-weight: 600; font-size: 9.5px; letter-spacing: 2.6px; color: var(--yellow);
  }
  .cam-frame { position: absolute; left: 730px; top: 58px; width: 443px; height: 267px; }
  .cam-name {
    position: absolute; left: 730px; top: 64px; width: 443px; text-align: center;
    font-weight: 800; font-size: 16px; letter-spacing: .5px; color: var(--white);
  }
  .social { position: absolute; left: 838px; width: 258px; height: 65px; }
  .social-top { position: absolute; inset: 0 0 32px 0; background: var(--panel-top); opacity: .9; }
  .social-bottom { position: absolute; left: 0; right: 0; top: 33px; bottom: 0; background: var(--panel-bottom); }
  .social-icon {
    position: absolute; left: 0; top: 0; width: 73px; height: 65px;
    background: linear-gradient(180deg, var(--yellow), #c79200);
  }
  .social-kicker {
    position: absolute; left: 111px; top: 14px;
    font-weight: 700; font-size: 9.5px; letter-spacing: 1.3px;
  }
  .social-label {
    position: absolute; left: 111px; top: 30px;
    font-weight: 900; font-size: 18px; letter-spacing: 1.6px;
  }
  .social--feed { top: 362px; }
  .social--chirp { top: 462px; }
  .social--donate { top: 559px; }
</style>
</head>
<body>
<main class="overlay">
  <section class="offline-screen" role="img" aria-label="Offline screen background with glowing yellow and orange shards on dark blue">
    <div class="offline-title">KORVINEQ</div>
    <div class="offline-status">CURRENTLY OFFLINE</div>
  </section>

  <svg class="cam-frame" viewBox="0 0 443 267" aria-hidden="true">
    <rect x="8" y="6" width="427" height="255" fill="#05081a"/>
    <rect x="8" y="4" width="427" height="5" fill="var(--navy)"/>
    <rect x="8" y="256" width="427" height="5" fill="var(--navy)"/>
    <polygon points="30,0 413,0 408,5 35,5" fill="var(--gold)"/>
    <polygon points="35,262 408,262 413,267 30,267" fill="var(--gold)"/>
    <polygon points="91,4 352,4 315,31 128,31" fill="var(--gold)"/>
    <polygon points="96,4 347,4 337,11 106,11" fill="var(--gold-light)"/>
    <polygon points="0,5 14,5 14,60 0,70" fill="var(--gold)"/>
    <polygon points="0,200 14,210 14,262 0,262" fill="var(--gold)"/>
    <polygon points="443,5 429,5 429,60 443,70" fill="var(--gold)"/>
    <polygon points="443,200 429,210 429,262 443,262" fill="var(--gold)"/>
    <rect x="7" y="78" width="2.5" height="112" fill="var(--gold)"/>
    <rect x="433.5" y="78" width="2.5" height="112" fill="var(--gold)"/>
    <g fill="#1a1a1a">
      <circle cx="7.5" cy="22" r="1.6"/><circle cx="7.5" cy="28" r="1.6"/><circle cx="7.5" cy="34" r="1.6"/>
      <circle cx="7.5" cy="227" r="1.6"/><circle cx="7.5" cy="233" r="1.6"/><circle cx="7.5" cy="239" r="1.6"/>
      <circle cx="435.5" cy="24" r="1.6"/><circle cx="435.5" cy="30" r="1.6"/><circle cx="435.5" cy="36" r="1.6"/>
      <circle cx="435.5" cy="229" r="1.6"/><circle cx="435.5" cy="235" r="1.6"/><circle cx="435.5" cy="241" r="1.6"/>
    </g>
  </svg>
  <div class="cam-name">KORVINE_Q</div>

  <div class="social social--feed">
    <div class="social-top"></div><div class="social-bottom"></div>
    <div class="social-icon"></div>
    <div class="social-kicker">FOLLOW ME ON</div>
    <div class="social-label">SNAPFEED</div>
  </div>
  <div class="social social--chirp">
    <div class="social-top"></div><div class="social-bottom"></div>
    <div class="social-icon"></div>
    <div class="social-kicker">FOLLOW ME ON</div>
    <div class="social-label">CHIRPLINE</div>
  </div>
  <div class="social social--donate">
    <div class="social-top"></div><div class="social-bottom"></div>
    <div class="social-icon" role="img" aria-label="Yellow skull emblem"></div>
    <div class="social-kicker">SUPPORT</div>
    <div class="social-label">DONATE</div>
  </div>
</main>
</body>
</html>
```